Nutritional & Gastrointestinal Health Consulting Service-Website design

We need a website design for a new health consulting service called "Bright Harbor" based in Perth, Australia.

We will be providing consulting services in the areas of:
1) Nutrition and Diet
2) Gastrointestinal Health (which means stomach & digestive system related health)

These consulting services will be provided by an Accredited Dietitian and a Paediatric Gastroenterologist.

We are open to creative ideas in terms of design, layout, fonts and colours. We also would love to see images of nature in the backdrop with families (adults with kids) having a good time, fresh fruits and vegetables displayed in a farmer's market or supermarket. 2 or 3 images should be sufficient. We would also definitely want our logo somewhere in the main page of website. The logo file is also attached. Please have a look at a website's design that we really liked. We would love to see designs inspired by that style. The website details are in the in the "nice to have priorities" section of this project brief.

We also would be looking at website designers with software coding skills so that if we like the design we can go ahead with the next step of coding.

The website design should communicate the purpose of the website and at the same time be simple, elegant and unique/eye-catching.

We look forward to receiving creative ideas for our website from you all. Good luck!
Updates

More details have been added to our project- for example: Logo, fonts style, must haves etc etc. Please view the updated project brief. Looking forward to receiving your fantastic ideas for our website. Thanking you

Hi, I have updated the colour preference. Will add the content preferences tomorrow. thanks

Hello all, I have now added a LOT more content to what we want in our website. It is very much in detail, so please carefully have a read through the entire project brief. If you have any questions write back to me and I will try to respond as quickly as I can. Last few days were busy so couldn't respond quickly to all of you who had send me designs/queries/questions. Thank you for your patience. I look forward to receiving fantastic designs from you all. Good Luck :-)

Target Market(s)

Adults based in western speaking countries aged 18 to 60 years

Industry/Entity Type

Software

Font styles to use
Sans Serif
Script

Colors
faa54b
acd036

Requirements
Must have
• The website must have the MAIN logo file attached. I have attached 3 files: 1) MAIN logo; 2) supplementary logo A ; 3) supplementary logo B

I have selected 2 colours from the colour scheme (see below)-(as the colour of our logo is that).
However we would also like to see LIGHT CHOCOLATE BROWN or CHOCOLATE BROWN colour used as the background colour of the website
Preferred WEBSITE CONTENT:
1) HOME PAGE:
Content required=
--Company Logo
--Dr Ravel Ostrin
Paediatric Gastroenterologist & Hepatologist
-Leora Ostrin.
Dietitian & Nutritionist
--Website Menu (either listed horizontally or vertically):
Once clicked on each name:

Under each of the Website Menu items we want the following Headings to be added

2) ABOUT US page:
Sub-heading under this: Qualification, Skills, Special Interest

3) SERVICES
RAVEL'S PAGE: Individual Consultation, Endoscopy procedures
Individual Consultation, Group Based Services, Food Diary, Food & Symptom Diary

4) FEES & REBATE: Content as below:
Please Note: Payment of full fees is required at the time of consultation and procedures. 48 hours notice is required for cancellation of appointments/non-attendance. Failure to provide this may result in a fee being incurred. Please call reception to find out the amount of fee charged for cancellation of appointments/non-attendance.
headings are:
Paediatric Gastroenterology:
Ravel's pge
Individual Consultation - Initial (upto 30 mins):
Review Consultation (upto 15 mins):
Endoscopy procedures - No Gap fees charged. Fees will be billed directly to Carewell. If any queries, please contact reception.

leora's pge
sub heading:
Individual Consultation - Initial (upto 45 mins):
Individual Consultation - Review (upto 30 mins):

Concession-Individual Consultation -Initial (upto 45 mins):
Concession-Individual Consultation - Review (upto 30 mins):
Please Note: Concession applies for health care card holders & pensioners

Group Based Services: Pricing subject to the type of service provided. Please contact us for an obligation free quote.
Education Topics Include:
- Paediatric Nutrition (Introducing Solids, Fussy Eating, Healthy Eating)
- Pregnancy Nutrition, Gestational Diabetes, Breastfeeding/Lactation Nutrition
- Healthy Eating, Supermarket Shopping Tips, Nutrition Label Reading Tips, Healthier
sub heading under nutrition & diet:
-Carewell:
--A rebate of $52.95 is available from Carewell if an EPC ( Enhanced Primary Care)/Chronic Disease Management (CDM) plan is issued by your GP.
--All mandatory paperwork needs to be available at the time of making your appointment for your eligibility.
-Private Health Fund:
--Most private health funds provide rebate on dietetic appointments. However the rebate amount depends on your level of cover. Thus, please contact your health fund to determine your entitled rebate.
-KRB: Approved provider for KRB services

6) FOR DOCTORS: Bright Harbor Paediatric Gastroenterologist Referral Form
Bright Harbor Dietitian Referral form
7) LOCATIONS & CONTACT

Paediatric Gastroenterology & Hepatology Service
Suite 82
Holloway Brenton Medical Centre
17 Quillan Fenwick Pde,
GLENDRA, WA 6177
P: (08) 9472 5031
F: (08) 9472 6640

Nutrition & Diet Service
Suite 82
17 Quillan Fenwick Pde,
GLENDRA, WA 6177
P: (08) 9472 5031
F: (08) 9472 6640

Tolliver Medical Centre
58-60 Corvane Parkway,
PELLARD, WA 6238
P: (08) 9627 4083
F: (08) 96274092
www.tmcpellard.com.au

This page should have a webform that has following titles:
-Your Name
-Your Email
-Your Phone
-Message

8) NEWS & BLOG
Nice to have
• We liked the design style of the websites below:
https://www.vivoraclinic.example/

http://tummywise.example/

But feel free to use your creativity too
Should not have
• Please do not use any body building or muscle building images

```html
<!DOCTYPE html>
<html lang="en">
<head>
<meta charset="utf-8">
<title>Bright Harbor</title>
<link rel="stylesheet" href="https://fonts.googleapis.com/css2?family=Open+Sans:wght@400;600;700&family=Lobster&family=Tinos:ital@1&display=swap">
<style>
:root{
  --orange:#faa54b;
  --orange-deep:#e8973f;
  --orange-dark:#e1920b;
  --green:#acd036;
  --brown:#4a3c33;
  --ink:#444;
  --line:#dcdcdc;
  --nav-bg:#f7f7f7;
  --page:#f1f1f1;
  --white:#fff;
}
*{box-sizing:border-box;margin:0;padding:0}
html,body{width:1200px;height:925px;overflow:hidden}
body{
  background:var(--page);
  background-image:repeating-linear-gradient(45deg,rgba(0,0,0,.018) 0 2px,transparent 2px 5px);
  font-family:"Open Sans",sans-serif;color:var(--ink);position:relative;
}
.site{position:absolute;left:110px;top:19px;width:980px;height:887px;background:var(--white);border:1px solid #e2e2e2}
.brand{position:absolute;left:20px;top:12px;display:flex;align-items:center;gap:10px}
.brand-mark{width:40px;height:40px;border-radius:50%;background:var(--orange)}
.brand-name{font-size:26px;font-weight:700;color:var(--green);letter-spacing:.5px;line-height:1}
.contact{position:absolute;top:19px;display:flex;align-items:center;gap:10px;font-size:12.5px;color:#555;white-space:nowrap}
.contact.phone{right:238px}
.contact.mail{right:17px}
.social{position:absolute;right:16px;top:58px;display:flex}
.social span{width:31px;height:31px;border:1px solid var(--line);margin-left:-1px;background:#f7f7f7}
.social span:first-child{background:#3b5998;border-color:#3b5998}
.nav{position:absolute;left:15px;top:97px;width:948px;height:60px;display:flex;border:1px solid var(--line);background:var(--nav-bg)}
.nav-home{width:82px;background:var(--orange);display:flex;align-items:center;justify-content:center;border-right:1px solid var(--orange-deep)}
.nav-home i{width:30px;height:30px;border-radius:50%;background:var(--white)}
.nav a{display:flex;align-items:center;justify-content:center;text-align:center;font-size:12.5px;color:#555;text-decoration:none;border-right:1px solid var(--line);line-height:1.25;text-transform:uppercase;white-space:nowrap}
.nav-search{width:48px;background:var(--orange);display:flex;align-items:center;justify-content:center}
.hero{position:absolute;left:16px;top:170px;width:947px;height:366px;overflow:hidden}
.hero-photo{position:absolute;inset:0;background:linear-gradient(100deg,#d9a08f 0%,#b46a78 25%,#8ea25f 55%,#6f8a3e 75%,#7b3a2a 100%)}
.hero-shade{position:absolute;inset:0;background:rgba(28,24,18,.78);clip-path:polygon(590px 0,947px 0,947px 366px,412px 366px)}
.hero-title{position:absolute;right:28px;top:86px;font-family:"Lobster",cursive;font-size:48px;font-weight:400;color:var(--orange);letter-spacing:1px}
.hero-text{position:absolute;left:555px;top:160px;width:358px;font-family:"Tinos",serif;font-style:italic;font-size:14.2px;line-height:18px;color:var(--white);text-align:justify}
.btn{position:absolute;left:805px;top:283px;width:107px;height:36px;border-radius:4px;background:linear-gradient(#f7b25e,var(--orange-deep));color:#3a2a1a;font-size:13px;display:flex;align-items:center;justify-content:center;box-shadow:0 2px 2px rgba(0,0,0,.3)}
.hero-arrows{position:absolute;left:0;bottom:0;display:flex}
.hero-arrows span{width:35px;height:31px;display:flex;align-items:center;justify-content:center;background:#2b2b2b}
.hero-arrows span:first-child{background:var(--orange-dark)}
.welcome{position:absolute;left:16px;top:541px;width:697px;height:294px;border:1px solid var(--line);overflow:hidden}
.welcome-photo{position:absolute;inset:0;background:linear-gradient(90deg,#e9ecef 0%,#f6efe8 35%,#f3e2cc 55%,#eef0f2 80%,#dfe6ec 100%)}
.welcome-band{position:absolute;left:0;top:134px;width:695px;height:92px;display:flex}
.welcome-title{width:284px;background:var(--brown);color:var(--white);padding:20px 0 0 16px}
.welcome-title small{display:block;font-size:16px;letter-spacing:.3px;border-bottom:2px solid var(--white);width:250px;padding:0 0 2px 6px;text-transform:uppercase}
.welcome-title strong{display:block;font-size:28px;font-weight:700;letter-spacing:.3px;line-height:32px;text-transform:uppercase;margin-left:4px;white-space:nowrap}
.welcome-text{flex:1;background:rgba(250,165,75,.9);color:var(--white);font-family:"Tinos",serif;font-style:italic;font-size:14.2px;line-height:18px;text-align:justify;padding:19px 16px 0 24px}
.help{position:absolute;left:727px;top:541px;width:236px;height:294px}
.help-photo{height:125px;background:linear-gradient(90deg,#c9d3dc,#e6dcd2 50%,#aebccb)}
.help-body{height:169px;background:var(--green);text-align:center;padding-top:10px}
.help svg{display:block;margin:0 auto}
.help h2{font-size:23px;font-weight:600;color:#333;width:200px;margin:0 auto 4px;border-bottom:2px solid #333;line-height:28px}
.help p{font-size:10.5px;line-height:13px;color:#333;padding:0 8px}
.footer{position:absolute;left:15px;top:842px;width:948px;height:33px;background:var(--orange-deep);color:var(--white);font-size:13px;display:flex;align-items:center;padding:0 15px}
</style>
</head>
<body>
<div class="site">
  <div class="brand"><span class="brand-mark"></span><span class="brand-name">BRIGHT HARBOR</span></div>

  <div class="contact phone">
    <svg width="16" height="20" viewBox="0 0 16 20"><path d="M4 1 L7 5 L5 8 Q7 12 10 14 L12 12 L15 15 L12 19 Q3 16 1 5 Z" fill="#faa54b"/></svg>
    Contact us: +000 555 210 487
  </div>
  <div class="contact mail">
    <svg width="22" height="16" viewBox="0 0 22 16"><rect x="1" y="3" width="20" height="12" fill="#faa54b"/><path d="M1 3 L11 10 L21 3" fill="none" stroke="#fff" stroke-width="1.5"/></svg>
    <span style="margin-left:4px">info@brightharbor.example</span>
  </div>
  <div class="social" aria-label="Social links"><span></span><span></span><span></span><span></span><span></span></div>

  <nav class="nav">
    <div class="nav-home"><i></i></div>
    <a href="#" style="width:184px">About Bright Harbor</a>
    <a href="#" style="width:92px">Services</a>
    <a href="#" style="width:97px">Product</a>
    <a href="#" style="width:172px">Accredited Dietitian</a>
    <a href="#" style="width:175px">Paediatric<br>Gastroenterologist</a>
    <a href="#" style="width:98px">Contact</a>
    <div class="nav-search"><svg width="12" height="12" viewBox="0 0 12 12"><circle cx="5" cy="5" r="3.5" fill="none" stroke="#fff" stroke-width="1.6"/><path d="M7.5 7.5 L11 11" stroke="#fff" stroke-width="1.8"/></svg></div>
  </nav>

  <section class="hero">
    <div class="hero-photo" role="img" aria-label="Mother and daughter choosing fresh fruit at a market"></div>
    <div class="hero-shade"></div>
    <h1 class="hero-title">Digestive Health</h1>
    <p class="hero-text">Lorem Ipsum is simply dummy text. Lorem Ipsum is simply dummy text. Lorem Ipsum is simply dummy text. Lorem Ipsum is simply dummy text. Lorem Ipsum is simply dummy text. Lorem Ipsum is simply dummy text. Lorem Ipsum is simply dummy text. Lorem Ipsum is simply dummy text.</p>
    <div class="btn">Read More</div>
    <div class="hero-arrows">
      <span><svg width="8" height="12" viewBox="0 0 8 12"><path d="M6 1 L1 6 L6 11" fill="none" stroke="#fff" stroke-width="1.5"/></svg></span>
      <span><svg width="8" height="12" viewBox="0 0 8 12"><path d="M2 1 L7 6 L2 11" fill="none" stroke="#fff" stroke-width="1.5"/></svg></span>
    </div>
  </section>

  <section class="welcome">
    <div class="welcome-photo" role="img" aria-label="Team of smiling medical staff in white coats"></div>
    <div class="welcome-band">
      <div class="welcome-title"><small>Welcome to</small><strong>Bright Harbor</strong></div>
      <p class="welcome-text">Lorem Ipsum is simply dummy text. Lorem Ipsum is simply dummy text. Lorem Ipsum is simply dummy text. Lorem Ipsum is simply dummy text.</p>
    </div>
  </section>

  <aside class="help">
    <div class="help-photo" role="img" aria-label="Support agent wearing a headset"></div>
    <div class="help-body">
      <svg width="64" height="58" viewBox="0 0 64 58"><ellipse cx="33" cy="26" rx="30" ry="24" fill="#333"/><path d="M10 40 L4 54 L22 46 Z" fill="#333"/><text x="33" y="37" text-anchor="middle" font-family="Open Sans, sans-serif" font-weight="700" font-size="32" fill="#acd036">?</text></svg>
      <h2>Online Help</h2>
      <p>Lorem Ipsum is simply dummy text. Lorem Ipsum is simply dummy text. Lorem Ipsum is simply dummy text.</p>
    </div>
  </aside>

  <footer class="footer">Copyright © 2014 All Right Reserved</footer>
</div>
</body>
</html>
```